10 Labels for Wild Bird Food

Label Design Request for New Products
We are excited to announce the launch of 10 new products and are seeking vibrant, fun, and colorful labels to match their energy. Each label should measure 6 x 4 inches (152.4mm x 101.6mm) and must feature our brand logo. Additionally, please include all the necessary information as detailed in the attached Word document.

Let's make our products stand out on the shelves with eye-catching designs!

Target Market(s)

Wild Bird Food Buyers

Requirements
Must have
• Logo

```html
<!DOCTYPE html>
<html lang="en">
<head>
<meta charset="utf-8">
<title>Meadow Perch – Wild Bird Food Labels</title>
<link rel="stylesheet" href="https://fonts.googleapis.com/css2?family=Roboto+Condensed:wght@400;500&family=Open+Sans:wght@400;700&family=Archivo:wght@800&display=swap">
<style>
  :root {
    --page-bg: #cccccc;
    --label-bg: #ffffff;
    --ink: #222222;
    --brand-teal: #1a8a7f;
    --brand-green: #8cc63f;
    --niger: #0e74bb;
    --wild: #8dc63f;
    --nomess: #2b3590;
    --peanut: #c89b6a;
    --sunflower: #333333;
  }
  * { box-sizing: border-box; margin: 0; padding: 0; }
  html, body { width: 1200px; height: 2398px; overflow: hidden; }
  body { background: var(--page-bg); position: relative; color: var(--ink); font-family: "Open Sans", sans-serif; }

  .label { position: absolute; width: 463px; height: 694px; background: var(--label-bg); }
  .label--r1c1 { left: 107px; top: 100px; }
  .label--r1c2 { left: 636px; top: 100px; }
  .label--r2c1 { left: 107px; top: 847px; }
  .label--r2c2 { left: 636px; top: 847px; }
  .label--r3 { left: 364px; top: 1606px; }

  .label__warnings { position: absolute; left: 26px; top: 28px; font: 500 13px/18px "Roboto Condensed", sans-serif; }
  .label__weight { position: absolute; right: 25px; top: 29px; font: 500 17px/20px "Roboto Condensed", sans-serif; }

  .brand { position: absolute; left: 0; right: 0; top: 118px; display: flex; justify-content: center; align-items: center; gap: 8px; }
  .brand__dot { width: 22px; height: 22px; border-radius: 50%; background: var(--brand-green); }
  .brand__name { font: 700 26px/30px "Open Sans", sans-serif; color: var(--brand-teal); }

  .label__band { position: absolute; left: 0; right: 0; top: 199px; height: 140px; display: flex; align-items: center; justify-content: center; }
  .label__title { font: 800 48px/46px "Archivo", Arial, sans-serif; color: #fff; text-align: center; letter-spacing: 2px; text-transform: uppercase; }
  .band--niger { background: var(--niger); }
  .band--wild { background: var(--wild); }
  .band--nomess { background: var(--nomess); }
  .band--peanut { background: var(--peanut); }
  .band--sunflower { background: var(--sunflower); }

  .label__rule { position: absolute; left: 26px; right: 26px; top: 383px; height: 3px; background: var(--ink); }

  .desc { position: absolute; left: 127px; width: 310px; bottom: 96px; font-size: 11.2px; line-height: 14.5px; }
  .desc__heading { font-weight: 700; margin-bottom: 4px; line-height: 13.5px; }
  .desc__sub { font-weight: 700; margin-top: 3px; }
  .desc__use { font-size: 11.8px; line-height: 15.3px; }

  .dates { position: absolute; left: 26px; top: 624px; width: 190px; height: 42px; border: 1.5px solid var(--ink); padding: 4px 6px; font: 400 10.5px/19px "Roboto Condensed", sans-serif; }
  .dates__row { display: flex; }
  .dates__key { width: 58px; }

  .maker { position: absolute; left: 255px; top: 614px; font: 500 10.3px/13.5px "Roboto Condensed", sans-serif; }
</style>
</head>
<body>

<section class="label label--r1c1">
  <p class="label__warnings">Not for human consumption<br>May Contain Nuts</p>
  <p class="label__weight">Net Wt: 3300g</p>
  <div class="brand"><span class="brand__dot"></span><span class="brand__name">Meadow Perch</span></div>
  <div class="label__band band--niger"><h2 class="label__title">Niger<br>Seed</h2></div>
  <div class="label__rule"></div>
  <div class="desc">
    <p class="desc__heading">Attract a Burst of Color to Your Garden with Nutritious Niger Seed!</p>
    <p>Invite a beautiful array of small, colorful birds to your garden with our Niger Seed 5L Bag, the top choice for bird enthusiasts who want to provide their feathered friends with a nutrient-rich and highly desirable treat. Known for its appeal to finches and other small birds, this premium bird seed will make your garden a lively and vibrant bird haven.</p>
    <p class="desc__sub">Easy to Use:</p>
    <p class="desc__use">Fill your nyjer seed feeders or sprinkle on bird tables to create an irresistible feast for your garden birds. Watch as they flock to your garden, bringing vibrant colors and cheerful chirping to your outdoor space.</p>
  </div>
  <div class="dates"><div class="dates__row"><span class="dates__key">Expiry Date</span>:</div><div class="dates__row"><span class="dates__key">Batch</span>:</div></div>
  <p class="maker">Meadow Perch<br>Alder Trading, Brookside Works Estate,<br>Oakhurst, OK4 2PL<br>Contact: sales@aldertrading.example</p>
</section>

<section class="label label--r1c2">
  <p class="label__warnings">Not for human consumption<br>May Contain Nuts</p>
  <p class="label__weight">Net Wt: 3300g</p>
  <div class="brand"><span class="brand__dot"></span><span class="brand__name">Meadow Perch</span></div>
  <div class="label__band band--wild"><h2 class="label__title">Wild<br>Bird Mix</h2></div>
  <div class="label__rule" style="top:371px"></div>
  <div class="desc">
    <p class="desc__heading">Transform Your Garden into a Bird Sanctuary with Our Nutritious Wild Bird Mix!</p>
    <p>Invite a diverse array of feathered friends to your garden with our Wild Bird Mix 5L Bag, the perfect choice for bird enthusiasts who want to provide their avian visitors with a balanced and tasty diet. Packed with a variety of high-quality seeds and grains, this premium bird food is designed to attract and nourish a wide range of bird species, ensuring your garden becomes a vibrant and lively haven.</p>
    <p class="desc__sub">Easy to Use:</p>
    <p class="desc__use">Fill your bird feeders, place on bird tables, or scatter on the ground to create an inviting space for birds. Watch as they flock to your garden, adding beauty and joyful song to your outdoor area.</p>
  </div>
  <div class="dates"><div class="dates__row"><span class="dates__key">Expiry Date</span>:</div><div class="dates__row"><span class="dates__key">Batch</span>:</div></div>
  <p class="maker">Meadow Perch<br>Alder Trading, Brookside Works Estate,<br>Oakhurst, OK4 2PL<br>Contact: sales@aldertrading.example</p>
</section>

<section class="label label--r2c1">
  <p class="label__warnings">Not for human consumption<br>May Contain Nuts</p>
  <p class="label__weight">Net Wt: 3200g</p>
  <div class="brand"><span class="brand__dot"></span><span class="brand__name">Meadow Perch</span></div>
  <div class="label__band band--nomess"><h2 class="label__title">No Mess Mix</h2></div>
  <div class="label__rule" style="top:382px"></div>
  <div class="desc">
    <p class="desc__heading">Enjoy a Clean and Vibrant Garden with Our Nutritious No Mess Mix!</p>
    <p>Invite a diverse array of beautiful birds to your garden without the hassle of leftover shells and debris with our No Mess Mix 5L Bag. This premium bird food is specially formulated to provide a nutritious, easy-to-eat blend that leaves no waste, ensuring your garden remains clean and your feathered visitors are well-fed.</p>
    <p class="desc__sub" style="margin-top:8px">Easy to Use:</p>
    <p class="desc__use">Fill your bird feeders, place on bird tables, or scatter on the ground to create an inviting and clean feeding space for birds. Watch as they flock to your garden, bringing vibrant colors and joyful chirping to your outdoor area</p>
  </div>
  <div class="dates"><div class="dates__row"><span class="dates__key">Expiry Date</span>:</div><div class="dates__row"><span class="dates__key">Batch</span>:</div></div>
  <p class="maker">Meadow Perch<br>Alder Trading, Brookside Works Estate,<br>Oakhurst, OK4 2PL<br>Contact: sales@aldertrading.example</p>
</section>

<section class="label label--r2c2">
  <p class="label__warnings">Not for human consumption<br>May Contain Nuts</p>
  <p class="label__weight">Net Wt: 2800g</p>
  <div class="brand"><span class="brand__dot"></span><span class="brand__name">Meadow Perch</span></div>
  <div class="label__band band--peanut"><h2 class="label__title">Peanut<br>Granules</h2></div>
  <div class="label__rule" style="top:386px"></div>
  <div class="desc">
    <p class="desc__heading">Nourish Your Garden Birds with Delicious, Nutritious Peanut Granules!</p>
    <p>Transform your garden into a vibrant bird sanctuary with our Peanut Granules 5L Bag, the perfect choice for bird enthusiasts who want to provide their avian visitors with a high-energy, nutrient-rich treat. Ideal for a wide variety of bird species, these premium peanut granules are sure to make your garden a favorite feeding spot</p>
    <p class="desc__sub">Easy to Use:</p>
    <p class="desc__use">Fill your bird feeders, sprinkle on bird tables, or mix with other bird food to create an irresistible feast for your garden birds. Watch as they flock to your garden, bringing vibrant colors and joyful chirping to your outdoor space</p>
  </div>
  <div class="dates"><div class="dates__row"><span class="dates__key">Expiry Date</span>:</div><div class="dates__row"><span class="dates__key">Batch</span>:</div></div>
  <p class="maker">Meadow Perch<br>Alder Trading, Brookside Works Estate,<br>Oakhurst, OK4 2PL<br>Contact: sales@aldertrading.example</p>
</section>

<section class="label label--r3">
  <p class="label__warnings">Not for human consumption<br>May Contain Nuts</p>
  <p class="label__weight">Net Wt: 2000g</p>
  <div class="brand"><span class="brand__dot"></span><span class="brand__name">Meadow Perch</span></div>
  <div class="label__band band--sunflower"><h2 class="label__title">Black<br>Sunflower</h2></div>
  <div class="label__rule" style="top:372px"></div>
  <div class="desc">
    <p class="desc__heading" style="font-size:12.5px;line-height:15px">Attract a Variety of Birds with Nutritious Black Sunflower Seeds!</p>
    <p>Turn your garden into a lively bird sanctuary with our Black Sunflower 5L Bag, the perfect choice for bird enthusiasts who want to provide their avian visitors with a nutritious and high-energy treat. Known for their high oil content and appeal to a wide range of bird species, these premium black sunflower seeds are sure to make your garden a favorite feeding spot.</p>
    <p class="desc__sub">Easy to Use:</p>
    <p class="desc__use">Fill your bird feeders, place on bird tables, or scatter on the ground to create an inviting space for birds. Watch as they flock to your garden, bringing vibrant colors and cheerful song to your outdoor area.</p>
  </div>
  <div class="dates"><div class="dates__row"><span class="dates__key">Expiry Date</span>:</div><div class="dates__row"><span class="dates__key">Batch</span>:</div></div>
  <p class="maker">Meadow Perch<br>Alder Trading, Brookside Works Estate,<br>Oakhurst, OK4 2PL<br>Contact: sales@aldertrading.example</p>
</section>

</body>
</html>
```